HR Outsourcing and Payroll Company needs a website re-design

The client is VireloStaffHR: www .virelostaff. example

They provide services to other businesses, specifically Human Resources (HR) Outsourcing and Payroll services. They are not happy with their current website and have retained our agency to provide a re-design.

You will design 4 pages for us to show the client. They will select a design they like. My agency will take the winning design and files and design the remaining pages of the site. But, we need you to help us establish a design for the basics so they can select a direction.

We need a Homepage design, a Service Page design, a Broker page design, and a Contact page design.

They really like these websites (in order from most preferred look and feel of imagery and design elements), so I think a mix between the two would be great:

https://www.brandleworks.example/
http://www.quopaly.example/

I have attached a project brief for this website. Please refer to it... It will help you be successful in what you deliver. The best designs will incorporate functionality and elements from the project brief.

Target Market(s)

Business owners. They will be thinking about thinks like employee reviews, payroll, time keeping, hiring, being compliant with state laws, and needing an expert to help them.

Industry/Entity Type

It Company

Number of Pages Required

4 page

Font styles to use
Sans Serif

Colors
f37122
0255a3
fbed22
9bcb3c
ec1f27

Requirements
Must have
• We need:
• -Homepage design (desktop and mobile)
• -Service Page design (desktop and mobile)
• -Broker page design (desktop and mobile)
• -Contact page design (desktop and mobile)
• Inspiration: a mix between the two would be great:
• https://www.brandleworks.example/
• http://www.quopaly.example/
• They like the long extended homepage look:
• http://www.quopaly.example/
• Photos that have focused people in the front and blurred backgrounds. Example: https://www.brandleworks.example/
• Graphic Icons for their services. Example:
• http://www.quopaly.example/
• I have attached a project brief for this website. Please refer to it... It will help you be successful in what you deliver. The best designs will incorporate functionality and elements from the project brief.
Should not have
• Crappy stock photos... you can use watermarked stock photos if you don't wish to purchase them for the sake of the contest.

```html
<!DOCTYPE html>
<html lang="en">
<head>
<meta charset="utf-8">
<title>VireloStaffHR – HR Outsourcing</title>
<link href="https://fonts.googleapis.com/css2?family=Open+Sans:wght@400;600;700&family=Roboto:wght@400;500&display=swap" rel="stylesheet">
<style>
:root{
  --bronze:#bf8139;
  --blue:#0255a3;
  --sand:#ead3b8;
  --cream:#f6e8dc;
  --cream-line:#e6cdb0;
  --ink:#111;
  --grey:#6b6b6b;
  --bar:#f7f7f7;
  --night:#141414;
  --white:#fff;
}
*{box-sizing:border-box;margin:0;padding:0}
html,body{width:1200px;height:1108px;overflow:hidden;background:var(--white)}
body{position:relative;font-family:"Open Sans",Arial,sans-serif;color:var(--ink)}
.abs{position:absolute}
.topbar{left:0;top:0;width:1200px;height:42px;background:var(--bar);border-bottom:1px solid #ddd}
.topbar .social{left:77px;top:12px;display:flex;gap:22px}
.topbar .social span{width:18px;height:18px;background:#555;border-radius:3px;display:block}
.topbar .social span:first-child{background:var(--blue)}
.search{left:876px;top:5px;width:248px;height:32px;display:flex;border:1px solid #ccc;background:#fff}
.search span{flex:1;font-size:15px;color:#777;padding:5px 10px}
.search i{width:35px;background:var(--bronze);display:flex;align-items:center;justify-content:center}
.brand{font-family:"Roboto",sans-serif;font-weight:500;font-size:34px;color:var(--blue);display:flex;align-items:center;gap:10px}
.brand b{width:14px;height:14px;border-radius:50%;background:var(--bronze);display:block}
.header .brand{left:77px;top:58px}
.call{right:76px;top:57px;display:flex;align-items:center;gap:9px;font-family:"Roboto",sans-serif}
.call .label{font-size:27px;color:var(--blue)}
.call .ring{width:52px;height:52px;border-radius:50%;border:1px solid #bbb;display:flex;align-items:center;justify-content:center}
.call .num{font-size:26px;font-weight:500;color:var(--blue)}
.nav{left:0;top:125px;width:1200px;height:57px;background:var(--bronze);font-family:"Roboto",sans-serif;font-size:20px;color:var(--white)}
.nav a{position:absolute;top:0;height:57px;line-height:57px;color:var(--white);text-decoration:none;text-align:center}
.nav a.active{background:var(--blue);width:121px;left:77px}
.page-title{left:100px;width:656px;top:220px;text-align:center;font-family:"Roboto",sans-serif;font-size:42px;font-weight:400}
.hero-art{left:340px;top:304px;width:139px;height:156px;border-radius:48% 48% 12px 12px;background:linear-gradient(160deg,#1b66b0,var(--blue))}
.copy{left:100px;top:478px;width:656px;height:250px;background:var(--cream);border:1px solid var(--cream-line);border-radius:8px;padding:12px 12px 0 12px;font-size:15px;line-height:27px;text-align:justify}
.copy p{text-indent:10px;margin-bottom:7px}
.services{left:775px;top:226px;width:348px;height:500px;background:var(--sand);border-radius:14px;overflow:hidden}
.services h2{height:63px;background:var(--bronze);text-align:center;font-family:"Roboto",sans-serif;font-weight:400;font-size:33px;line-height:63px;color:var(--ink)}
.services h2 em{font-style:normal;color:var(--white)}
.service{position:absolute;left:10px;width:340px;height:83px}
.service .badge{position:absolute;left:0;top:0;width:73px;height:73px;border-radius:50%;background:var(--white);display:flex;align-items:center;justify-content:center}
.service .badge i{width:36px;height:36px;border-radius:8px;background:var(--blue);display:block}
.service .badge i.warm{background:var(--bronze)}
.service h3{position:absolute;left:89px;top:0;font-family:"Roboto",sans-serif;font-weight:400;font-size:23px;color:var(--bronze);white-space:nowrap}
.service h3.current{color:var(--ink)}
.service p{position:absolute;left:90px;top:29px;width:230px;font-size:16px;line-height:21px;color:var(--grey)}
.footer{left:0;top:788px;width:1200px;height:272px;background:var(--night);color:var(--white)}
.footer h4{position:absolute;top:20px;font-family:"Roboto",sans-serif;font-weight:400;font-size:21px}
.footer .brand{left:77px;top:66px;font-size:30px}
.f-social{left:77px;top:167px;display:flex;gap:22px}
.f-social span{width:52px;height:52px;border-radius:50%;background:var(--white);display:block}
.f-social span:first-child{background:var(--blue)}
.links{left:350px;top:66px;list-style:none;font-size:16px;line-height:26px}
.field{left:620px;width:234px;height:41px;border:2px solid #ccc;background:var(--white);font-size:16px;color:#333;padding:8px 4px}
.subscribe{left:620px;top:201px;width:146px;height:41px;background:var(--white);color:var(--blue);font-family:"Roboto",sans-serif;font-size:19px;text-align:center;line-height:41px}
.contact{left:890px;top:66px;width:230px;font-size:16px}
.contact li{list-style:none;display:flex;gap:8px;margin-bottom:8px;line-height:25px}
.contact svg{flex:none;margin-top:4px}
.contact .muted{color:#ccc}
.legal{left:0;top:1060px;width:1200px;height:48px;background:var(--bronze);color:var(--white);font-size:16px;line-height:48px}
.legal .left{position:absolute;left:79px}
.legal .right{position:absolute;right:77px}
.legal .right span{margin:0 16px;opacity:.6}
</style>
</head>
<body>

<div class="abs topbar">
  <div class="abs social" aria-label="Social links"><span></span><span></span><span></span><span></span></div>
  <div class="abs search"><span>Search here...</span><i><svg width="16" height="16" viewBox="0 0 16 16"><circle cx="6.5" cy="6.5" r="4.8" fill="none" stroke="#fff" stroke-width="2"/><line x1="10" y1="10" x2="14.5" y2="14.5" stroke="#fff" stroke-width="2.4"/></svg></i></div>
</div>

<header class="header">
  <div class="abs brand"><b></b>VireloStaffHR</div>
  <div class="abs call">
    <span class="label">Call us now</span>
    <span class="ring"><svg width="22" height="22" viewBox="0 0 24 24"><path d="M6.6 10.8a15 15 0 0 0 6.6 6.6l2.2-2.2c.3-.3.7-.4 1-.2 1.1.4 2.3.6 3.6.6.6 0 1 .4 1 1V20c0 .6-.4 1-1 1A17 17 0 0 1 3 4c0-.6.4-1 1-1h3.5c.6 0 1 .4 1 1 0 1.3.2 2.5.6 3.6.1.3 0 .7-.2 1z" fill="#111"/></svg></span>
    <span class="num">123 456 7890</span>
  </div>
</header>

<nav class="abs nav">
  <a class="active" href="#">HOME</a>
  <a href="#" style="left:234px">ABOUT</a>
  <a href="#" style="left:368px">SERVICES</a>
  <a href="#" style="left:528px">BROKER</a>
  <a href="#" style="left:674px">RESOURCES</a>
  <a href="#" style="left:854px">BLOG</a>
  <a href="#" style="left:973px">CONTACT</a>
</nav>

<h1 class="abs page-title">HR Outsourcing</h1>
<div class="abs hero-art" role="img" aria-label="Blue icon of a business person with a dollar badge"></div>

<div class="abs copy">
  <p>Lorem Ipsum is simply dummy text of the printing and typesetting industry. Lorem Ipsum has been the industry's standard dummy text ever since the 1500s, when an unknown printer took a galley of type and scrambled it to make a type specimen book. It has survived not only five centuries, but also the leap into electronic typesetting,</p>
  <p>Lorem Ipsum is simply dummy text of the printing and typesetting industry. Lorem Ipsum has been the industry's standard dummy text ever since the 1500s, when an unknown printer took a galley of type and scrambled it to make a type specimen book. It has survived not only five centuries, but also the leap into electronic typesetting,</p>
</div>

<aside class="abs services">
  <h2><em>OUR</em> SERVICES</h2>
  <div class="service" style="top:76px"><div class="badge"><i role="img" aria-label="HR outsourcing icon"></i></div><h3>HR Outsourcing</h3><p>Lorem Ipsum is simply dummy text of the print ing and...</p></div>
  <div class="service" style="top:159px"><div class="badge"><i role="img" aria-label="Safety shield icon"></i></div><h3>Safety</h3><p>Lorem Ipsum is simply dummy text of the print ing and...</p></div>
  <div class="service" style="top:242px"><div class="badge"><i class="warm" role="img" aria-label="Payroll icon"></i></div><h3 class="current">Payroll / Timekeeping</h3><p>Lorem Ipsum is simply dummy text of the print ing and...</p></div>
  <div class="service" style="top:325px"><div class="badge"><i role="img" aria-label="Benefits administration icon"></i></div><h3>Benefits&nbsp; Administration</h3><p>Lorem Ipsum is simply dummy text of the print ing and...</p></div>
  <div class="service" style="top:408px"><div class="badge"><i role="img" aria-label="Workers' compensation icon"></i></div><h3>Workers’ Compensation</h3><p>Lorem Ipsum is simply dummy text of the print ing and...</p></div>
</aside>

<footer class="abs footer">
  <div class="abs brand"><b></b>VireloStaffHR</div>
  <div class="abs f-social" aria-label="Social links"><span></span><span></span><span></span></div>

  <h4 style="left:350px">Useful Links</h4>
  <ul class="abs links"><li>Home</li><li>About</li><li>Services</li><li>Broker</li><li>Resources</li><li>Blog</li><li>Contact</li></ul>

  <h4 style="left:621px">Newsletter</h4>
  <div class="abs field" style="top:71px">Enter Name</div>
  <div class="abs field" style="top:136px">Enter Email</div>
  <div class="abs subscribe">SUBSCRIBE</div>

  <h4 style="left:892px">Get In Touch With Us</h4>
  <ul class="abs contact">
    <li><svg width="14" height="18" viewBox="0 0 14 18"><path d="M7 0a7 7 0 0 0-7 7c0 5 7 11 7 11s7-6 7-11a7 7 0 0 0-7-7zm0 9.5A2.5 2.5 0 1 1 7 4.5a2.5 2.5 0 0 1 0 5z" fill="#fff"/></svg><span>Lorem Ipsum is simply dummy text of the printing and typesetting.</span></li>
    <li><svg width="18" height="18" viewBox="0 0 24 24"><path d="M6.6 10.8a15 15 0 0 0 6.6 6.6l2.2-2.2c.3-.3.7-.4 1-.2 1.1.4 2.3.6 3.6.6.6 0 1 .4 1 1V20c0 .6-.4 1-1 1A17 17 0 0 1 3 4c0-.6.4-1 1-1h3.5c.6 0 1 .4 1 1 0 1.3.2 2.5.6 3.6.1.3 0 .7-.2 1z" fill="#fff"/></svg><strong class="muted">123 456 7890</strong></li>
    <li><svg width="18" height="14" viewBox="0 0 18 14"><rect x="1" y="1" width="16" height="12" fill="none" stroke="#fff" stroke-width="1.6"/><path d="M1 1l8 7 8-7" fill="none" stroke="#fff" stroke-width="1.6"/></svg><span class="muted">Lorem Ipsum is simply</span></li>
    <li><svg width="18" height="18" viewBox="0 0 18 18"><circle cx="9" cy="9" r="7.5" fill="none" stroke="#fff" stroke-width="1.4"/><ellipse cx="9" cy="9" rx="3.5" ry="7.5" fill="none" stroke="#fff" stroke-width="1.2"/><line x1="1.5" y1="9" x2="16.5" y2="9" stroke="#fff" stroke-width="1.2"/></svg><span class="muted">Lorem Ipsum is simply</span></li>
  </ul>
</footer>

<div class="abs legal">
  <div class="left">© <strong>VIRELOSTAFFHR</strong> - 2016. All Rights Reserved.</div>
  <div class="right">Privacy&nbsp; policy<span>|</span>Terms&nbsp; of Use</div>
</div>

</body>
</html>
```